Stationery Design Project

We need a stationary design (business card, logo, letterhead) for a new company called "Meridel Kestrova".
We provide software and consulting services to improve business efficiency & increase team engagement.
We focus on workflow automation, business social networking software and collaboration and communication tools built on mobile platforms.
Updates

Target Market(s)

Business with multi-site,young, mobile workforces e.g Retailers, Hospitality

Industry/Entity Type

Communication

Requirements
Must have
• Letterhead to include;
Business Address: 17 Wendle St, Corvath Vale, NSW 2100
ABN : 48 615 207 392

```html
<!DOCTYPE html>
<html lang="en">
<head>
<meta charset="utf-8">
<title>Meridel Kestrova — Stationery</title>
<link rel="stylesheet" href="https://fonts.googleapis.com/css2?family=Open+Sans:wght@400;600&display=swap">
<style>
  :root {
    --board-blue: #0b3f8c;
    --card-navy: #36559b;
    --accent-blue: #4a90d9;
    --mark-blue: #3d68b3;
    --ink: #3a3a3a;
    --ink-soft: #555555;
    --paper: #ffffff;
  }
  * { box-sizing: border-box; margin: 0; padding: 0; }
  html, body { width: 1200px; height: 900px; overflow: hidden; }
  body {
    position: relative;
    background: var(--board-blue);
    font-family: "Open Sans", Arial, sans-serif;
    color: var(--ink);
  }
  .brand {
    display: flex;
    align-items: center;
    justify-content: center;
    gap: 8px;
    font-weight: 600;
    text-transform: uppercase;
    letter-spacing: 0.08em;
    line-height: 1.15;
  }
  .brand-dot {
    flex: none;
    background: var(--mark-blue);
    border-radius: 50%;
  }
  .board-brand {
    position: absolute;
    left: 38px; top: 100px;
    color: var(--paper);
    font-size: 22px;
    justify-content: flex-start;
  }
  .board-brand .brand-dot { width: 18px; height: 18px; background: var(--accent-blue); }

  .card {
    position: absolute;
    left: 146px;
    width: 338px;
    height: 192px;
  }
  .card-front {
    top: 339px;
    background: var(--paper);
    text-align: center;
  }
  .card-front .brand {
    margin-top: 62px;
    font-size: 15px;
    color: var(--ink);
  }
  .card-front .brand-dot { width: 12px; height: 12px; }
  .card-person {
    margin-top: 22px;
    font-size: 13px;
    color: var(--ink);
  }
  .card-person .person-name { color: var(--accent-blue); text-transform: uppercase; }
  .card-contact {
    margin-top: 8px;
    font-size: 8.4px;
    line-height: 1.35;
    color: var(--ink-soft);
  }
  .card-contact .web { color: var(--accent-blue); }

  .card-back {
    top: 555px;
    background: var(--card-navy);
    display: flex;
    align-items: center;
    justify-content: center;
  }
  .card-back .brand { color: var(--paper); font-size: 17px; }
  .card-back .brand-dot { width: 14px; height: 14px; background: var(--paper); }

  .letterhead {
    position: absolute;
    left: 573px; top: 93px;
    width: 526px; height: 740px;
    background: var(--paper);
  }
  .letterhead .brand {
    margin-top: 80px;
    font-size: 11px;
    color: var(--ink);
  }
  .letterhead .brand-dot { width: 9px; height: 9px; }
  .letterhead-footer {
    position: absolute;
    left: 0; right: 0; bottom: 30px;
    text-align: center;
    font-size: 7px;
    line-height: 1.45;
    color: var(--ink-soft);
  }
</style>
</head>
<body>
  <div class="brand board-brand"><span class="brand-dot"></span><span>Meridel Kestrova</span></div>

  <section class="card card-front">
    <div class="brand"><span class="brand-dot"></span><span>Meridel Kestrova</span></div>
    <p class="card-person"><span class="person-name">Dara Holvin</span> / Managing Director</p>
    <p class="card-contact">
      T: +61 2 8114 5072; M: +61 427 390 518; E: dara.holvin@meridelkestrova.com<br>
      <span class="web">www.meridelkestrova.com</span>
    </p>
  </section>

  <section class="card card-back">
    <div class="brand"><span class="brand-dot"></span><span>Meridel Kestrova</span></div>
  </section>

  <section class="letterhead">
    <div class="brand"><span class="brand-dot"></span><span>Meridel Kestrova</span></div>
    <p class="letterhead-footer">
      Business Address: 17 Wendle St, Corvath Vale, NSW 2100<br>
      ABN : 48 615 207 392
    </p>
  </section>
</body>
</html>
```